bmlk website

revamp of existing website...design only
brimlake.com.au
existing site a bit óld fashioned'...needs to be modernised and bright and cheery.
need: home page, second and third level pages.

end user/retail information website
this site does NOT need a shopping card as we do not sell direct to the public

• 3 levels
• home
• second level
• third level

```html
<!DOCTYPE html>
<html lang="en">
<head>
<meta charset="utf-8">
<title>Brimlake – Metal Storage Cabinets</title>
<link rel="stylesheet" href="https://fonts.googleapis.com/css2?family=Noto+Sans:wght@400;700&display=swap">
<style>
:root{
  --plate-dark:#1c1c1c;
  --plate-mid:#3a3a3a;
  --page:#ededed;
  --page-light:#f6f6f6;
  --red:#d42020;
  --red-dark:#b71515;
  --ink:#3b3530;
  --body:#222;
  --muted:#444;
  --white:#fff;
  --line:#d4d4d4;
  --gold:#d4a52a;
  --font:"Noto Sans",Tahoma,Verdana,sans-serif;
}
*{box-sizing:border-box;margin:0;padding:0}
html,body{width:1200px;height:1023px;overflow:hidden}
body{position:relative;background:var(--page);font-family:var(--font);color:var(--body)}
.site-header{position:absolute;left:0;top:0;width:1200px;height:168px;z-index:1;
  background:radial-gradient(ellipse at 50% 40%,var(--plate-mid),var(--plate-dark) 75%);
  border-bottom:1px solid #000}
.origin-badge{position:absolute;left:178px;top:8px;width:136px;height:118px;border-radius:14px;
  background:linear-gradient(160deg,#c8232c,#1f3a8a 60%)}
.brand-name{position:absolute;left:328px;top:36px;font-size:42px;font-weight:700;color:var(--white);letter-spacing:1px}
.top-nav{position:absolute;left:767px;top:17px;width:257px;height:38px;background:#000;border-radius:12px;
  border:1px solid #555;display:flex;align-items:center;justify-content:space-around;padding:0 8px}
.top-nav a{color:var(--white);text-decoration:none;font-size:13px}
.contact{position:absolute;left:788px;color:var(--white);font-size:13px;display:flex;align-items:center;gap:8px;letter-spacing:.3px}
.contact svg{width:18px;height:14px}
.main-nav{position:absolute;left:176px;top:134px;width:848px;height:64px;border-radius:10px;z-index:10;
  background:linear-gradient(#e92a2a,var(--red-dark));border:3px solid #eee;box-shadow:0 3px 4px rgba(0,0,0,.35);
  display:flex;align-items:center;justify-content:space-around;padding:0 12px}
.main-nav a{color:var(--white);text-decoration:none;font-size:13px;letter-spacing:.5px}
.hero{position:absolute;left:0;top:169px;width:1200px;height:380px;
  background:linear-gradient(#dedede,var(--page) 25%,var(--page));border-bottom:1px solid var(--line)}
.hero-title{position:absolute;left:176px;top:97px;font-size:24px;font-weight:400;color:var(--ink)}
.hero-text{position:absolute;left:176px;top:145px;width:475px;font-size:13px;line-height:21.5px;color:var(--body);letter-spacing:.5px}
.btn{position:absolute;top:258px;width:133px;height:33px;border-radius:6px;border:3px solid #f2f2f2;
  box-shadow:0 2px 3px rgba(0,0,0,.4);color:var(--white);font-size:15px;text-align:center;line-height:27px;text-decoration:none}
.btn-buy{left:177px;background:linear-gradient(#ea3030,var(--red-dark))}
.btn-detail{left:318px;background:linear-gradient(#3a3a3a,#0d0d0d)}
.hero-photo{position:absolute;left:692px;top:63px;width:252px;height:253px;background:linear-gradient(90deg,#e2e2e2,#d3d3d3 60%,#c0c0c0)}
.guarantee{position:absolute;left:855px;top:211px;width:142px;height:139px;border-radius:50%;
  background:radial-gradient(circle,#f3d36b,var(--gold) 70%,#9a741b)}
.features{position:absolute;left:176px;top:570px;width:217px;height:351px;border:1px solid #ddd;border-radius:8px;
  background:linear-gradient(var(--page-light),#e4e4e4)}
.features h2{font-size:19px;font-weight:400;color:var(--ink);text-align:center;padding:10px 0 8px}
.features ul{list-style:none}
.features li{position:relative;padding:8px 14px 8px 29px;font-size:13px;line-height:21.5px;letter-spacing:.5px;text-align:justify;border-top:1px solid #fafafa;border-bottom:1px solid #d8d8d8}
.features li::before{content:"";position:absolute;left:11px;top:16px;width:7px;height:7px;border-radius:50%;background:#9a1e1e}
.about-title{position:absolute;left:416px;top:581px;font-size:19px;font-weight:400;color:var(--ink)}
.about-text{position:absolute;left:414px;top:622px;width:611px;font-size:13px;line-height:21.5px;letter-spacing:.45px;color:var(--muted);text-align:justify}
.product{position:absolute;top:713px;width:200px;height:200px;background:var(--white);border:1px solid var(--line);padding:12px 24px}
.product div{width:100%;height:100%}
.site-footer{position:absolute;left:0;top:950px;width:1200px;height:73px;
  background:radial-gradient(ellipse at 50% 50%,var(--plate-mid),var(--plate-dark) 75%);border-top:1px solid #000;
  color:var(--white);font-size:13px;text-align:center;padding-top:20px;letter-spacing:.2px}
.site-footer span{color:#e51c1c}
</style>
</head>
<body>
<header class="site-header">
  <div class="origin-badge" role="img" aria-label="Map of Australia with flag, made in Australia for over 35 years"></div>
  <div class="brand-name">Brimlake</div>
  <nav class="top-nav"><a href="#">Home</a><a href="#">About Us</a><a href="#">Where to Buy</a></nav>
  <div class="contact" style="top:72px"><svg viewBox="0 0 18 14"><path d="M1 4c0-3 16-3 16 0v2h-4V4H5v2H1z M4 7h10l2 6H2z" fill="#fff"/></svg>1300 555 019</div>
  <div class="contact" style="top:97px"><svg viewBox="0 0 18 14"><rect x="1" y="1" width="16" height="12" fill="#fff"/><path d="M1 1l8 7 8-7" stroke="#333" fill="none"/></svg>info@brimlake.com</div>
</header>
<nav class="main-nav">
  <a href="#">STYLE 1</a><a href="#">STYLE 2</a><a href="#">STYLE 3</a><a href="#">COUNTER HEIGHT</a><a href="#">HALF WIDTH</a><a href="#">STYLE 5K</a><a href="#">STYLE 6K</a>
</nav>
<section class="hero">
  <h1 class="hero-title">METAL STORAGE CABINETS</h1>
  <p class="hero-text">Whether it be tiding the garage, organising the shed, re-arranging the archives, Brimlake has a unit to suit. Tough enough for the garage and aesthetically pleasing enough for the office.<br>Browse the website...there is sure to be one to suit your space !</p>
  <a class="btn btn-buy" href="#">BUY NOW</a>
  <a class="btn btn-detail" href="#">DETAIL</a>
  <div class="hero-photo" role="img" aria-label="Pair of white metal storage cabinets, one open with files and boxes on shelves"></div>
  <div class="guarantee" role="img" aria-label="Gold guarantee seal"></div>
</section>
<aside class="features">
  <h2>Key Features</h2>
  <ul>
    <li>Perfect for brooms, shovels mops, garden rakes</li>
    <li>Don't need doors... then this is the unit for you</li>
    <li>The clear span shelves make this the most popular unit</li>
    <li>3 sizes in all galvanised units</li>
  </ul>
</aside>
<h2 class="about-title">About Brimlake</h2>
<p class="about-text">Lorem ipsum dolor sit amet, consectetur adipiscing elit. Suspendisse gravida justo est. Sed varius, arcu eu hendrerit facilisis, enim purus viverra tellus, vitae vestibulum lectus sem non mi. Vivamus at urna risus, tincidunt pharetra arcu.</p>
<div class="product" style="left:414px"><div role="img" aria-label="Light grey cabinet with doors open" style="background:linear-gradient(90deg,#d8d8d8,#c4c4c4)"></div></div>
<div class="product" style="left:619px"><div role="img" aria-label="Tall white cabinet with one door open" style="background:linear-gradient(90deg,#e0e0e0,#c8c8c8)"></div></div>
<div class="product" style="left:824px"><div role="img" aria-label="Dark grey cabinet with shelves, hanging space and drawers" style="background:linear-gradient(90deg,#6a6f70,#4e5354)"></div></div>
<footer class="site-footer">Copyright <span>Brimlake</span>, All Rights Reserved</footer>
</body>
</html>
```